Creative, Colorful, Dynamic Infographic for Global Non-Profit

We are a global arts and education non-profit in need of an infographic that illustrates four key skills embedded in our work: Curiosity, Listening, Imagination, Postive Action.
We work primarily with educators, students, and artists who use the power of personal stories to build community and connection and to bridge divides.
Our new brand guidelines, logos, and fonts are here: https://stylekit.example/quillbridge-7
I've attached a mock-up of the graphic and the required text. (Note the attached design was created by a staff person, your final design does not need to be the same. The color scheme and text of the final design should match the brand guidelines above.)
The graphic will be used for both web and print media and should include the purple Quillbridge 7 logo (also attached).
Ideally the final design will delight audiences and spark interest in our work.

```html
<!DOCTYPE html>
<html lang="en">
<head>
<meta charset="utf-8">
<title>Quillbridge 7 — Four Key Skills</title>
<link rel="stylesheet" href="https://fonts.googleapis.com/css2?family=Fira+Sans:ital,wght@0,400;0,600;1,400&display=swap">
<style>
  :root {
    --green: #4cb78c;
    --green-soft: #a9d5c1;
    --orange: #f49755;
    --orange-soft: #f9c59f;
    --red: #ef4546;
    --red-soft: #f6a18e;
    --blue: #2a69b3;
    --blue-soft: #7ca9da;
    --purple: #663695;
    --ink: #1a1a1a;
    --white: #ffffff;
  }
  * { box-sizing: border-box; margin: 0; padding: 0; }
  html, body { width: 1200px; height: 1199px; overflow: hidden; background: var(--white); }
  .canvas { position: relative; width: 1200px; height: 1199px; font-family: "Fira Sans", sans-serif; }
  .diagram { position: absolute; inset: 0; }
  .skill-icon { position: absolute; width: 84px; height: 84px; }
  .skill-label {
    position: absolute; height: 31px; line-height: 31px; padding: 0 10px;
    background: var(--white); border-radius: 16px;
    font-weight: 600; font-size: 23px; letter-spacing: 0.2px;
    transform: translateX(-50%);
    white-space: nowrap;
  }
  .skill-text {
    position: absolute; width: 300px; transform: translateX(-50%);
    text-align: center; color: var(--white);
    font-weight: 600; font-size: 20px; line-height: 25.5px;
  }
  .curiosity .skill-label { color: var(--green); }
  .action .skill-label { color: var(--orange); }
  .listening .skill-label { color: var(--red); }
  .imagination .skill-label { color: var(--blue); }
  .link-text {
    position: absolute; transform: translateX(-50%);
    text-align: center; color: var(--ink);
    font-style: italic; font-size: 18.5px; line-height: 21.7px; white-space: nowrap;
  }
  .brand-name {
    position: absolute; left: 602px; top: 602px; transform: translate(-50%, -50%);
    color: var(--white); font-weight: 600; font-size: 24px; line-height: 28px;
    text-align: center; width: 160px;
  }
</style>
</head>
<body>
<main class="canvas">
  <svg class="diagram" width="1200" height="1199" viewBox="0 0 1200 1199" aria-hidden="true">
    <!-- connecting arrows -->
    <polygon fill="var(--orange-soft)" points="760,300 548,300 548,267 467,345 548,423 548,390 760,390"/>
    <polygon fill="var(--green-soft)" points="237,470 350,470 350,598 391,598 293,680 195,598 237,598"/>
    <polygon fill="var(--red-soft)" points="430,812 657,812 657,779 737,857 657,933 657,901 430,901"/>
    <polygon fill="var(--blue-soft)" points="855,740 855,603 813,603 911,525 1009,603 968,603 968,740"/>
    <!-- skill circles -->
    <circle cx="293" cy="345" r="160" fill="var(--green-soft)"/>
    <circle cx="293" cy="345" r="150" fill="var(--green)"/>
    <circle cx="911" cy="345" r="160" fill="var(--orange-soft)"/>
    <circle cx="911" cy="345" r="150" fill="var(--orange)"/>
    <circle cx="293" cy="857" r="160" fill="var(--red-soft)"/>
    <circle cx="293" cy="857" r="150" fill="var(--red)"/>
    <circle cx="911" cy="862" r="160" fill="var(--blue-soft)"/>
    <circle cx="911" cy="862" r="150" fill="var(--blue)"/>
    <!-- brand circle -->
    <circle cx="602" cy="602" r="98" fill="var(--purple)"/>
  </svg>

  <section class="skill curiosity">
    <svg class="skill-icon" style="left:251px;top:217px" viewBox="0 0 84 84" fill="none" stroke="#fff" stroke-width="2.5" aria-hidden="true">
      <path d="M42 4a37 37 0 1 1-22 67L6 75l6-13A37 37 0 0 1 42 4z"/>
      <path d="M32 32a10 10 0 1 1 14 9c-3 2-4 4-4 8" stroke-width="4" stroke-linecap="round"/>
      <circle cx="42" cy="58" r="2.5" fill="#fff" stroke="none"/>
    </svg>
    <div class="skill-label" style="left:293px;top:316px">CURIOSITY</div>
    <p class="skill-text" style="left:293px;top:352px">Focus on how you can learn<br>from another’s knowledge<br>and experience.</p>
  </section>

  <section class="skill action">
    <svg class="skill-icon" style="left:869px;top:230px" viewBox="0 0 84 84" fill="none" stroke="#fff" stroke-width="2.5" stroke-linecap="round" aria-hidden="true">
      <path d="M14 30a30 30 0 0 1 20-17M50 13a30 30 0 0 1 20 17M70 54a30 30 0 0 1-20 17M34 71a30 30 0 0 1-20-17"/>
      <circle cx="42" cy="42" r="17"/>
      <path d="M34 42l6 6 10-11"/>
      <path d="M12 12l12 12M24 17v7h-7M72 12L60 24M60 17v7h7M12 72l12-12M17 60h7v7M72 72L60 60M67 60h-7v7"/>
    </svg>
    <div class="skill-label" style="left:911px;top:332px">POSITIVE ACTION</div>
    <p class="skill-text" style="left:911px;top:368px">Show your words<br>and actions matter.</p>
  </section>

  <section class="skill listening">
    <svg class="skill-icon" style="left:251px;top:749px" viewBox="0 0 84 84" fill="none" stroke="#fff" stroke-width="2.5" stroke-linecap="round" aria-hidden="true">
      <circle cx="42" cy="42" r="39"/>
      <path d="M22 34a12 12 0 1 1 22 6c-3 4-6 5-6 10s-4 9-9 7"/>
      <path d="M28 35a5 5 0 1 1 8 4c-2 1-3 3-2 5"/>
      <path d="M52 34c2 3 2 7 0 10M58 30c4 5 4 13 0 18M64 26c6 7 6 19 0 26"/>
    </svg>
    <div class="skill-label" style="left:293px;top:848px">LISTENING</div>
    <p class="skill-text" style="left:293px;top:884px">Seek to understand<br>before speaking.</p>
  </section>

  <section class="skill imagination">
    <svg class="skill-icon" style="left:869px;top:726px" viewBox="0 0 84 84" fill="none" stroke="#fff" stroke-width="2.5" stroke-linecap="round" aria-hidden="true">
      <path d="M42 2v6M22 8l3 5M62 8l-3 5M10 20l5 3M74 20l-5 3M4 40h7M80 40h-7"/>
      <path d="M30 62c0-8-10-12-10-24a22 22 0 0 1 44 0c0 12-10 16-10 24z"/>
      <path d="M32 67h20M34 72h16M38 77h8"/>
      <circle cx="42" cy="38" r="5"/>
      <circle cx="42" cy="38" r="11" stroke-dasharray="4 3"/>
    </svg>
    <div class="skill-label" style="left:911px;top:847px">IMAGINATION</div>
    <p class="skill-text" style="left:911px;top:883px">Consider possibilities<br>beyond what you know.</p>
  </section>

  <p class="link-text" style="left:645px;top:313px">Your positive actions<br>lead to curiosity about<br>what else is possible.</p>
  <p class="link-text" style="left:293px;top:512px">Your<br>curiosity<br>allows you<br>to listen.</p>
  <p class="link-text" style="left:559px;top:825px">Your listening allows<br>you to take in<br>new information.</p>
  <p class="link-text" style="left:913px;top:581px">Your<br>imagination<br>can spark<br>positive<br>action.</p>

  <div class="brand-name">Quillbridge 7</div>
</main>
</body>
</html>
```